Stationary Set Rebrand for Brenvik

We are a Canadian Distribution and Service Company that was established in 1969. Over the past 5 decades we have expanded our business and have warehouses across Canada. We specialize in adhesive tapes, adhesives, films, safety, warehouse, shipping, janitorial and packaging supplies.

We have updated our logo design and would like a new corporate branding identity that includes a new fresh Stationary Set (Business Cards, Letterhead, Letterhead MS Word, Envelope, Presentation Folders, Email Signatures, Notepad Covers, etc.)

Target Market(s)

Industrial Business Sector

Font styles to use
Sans Serif

Colors
0054AA
0677BA
7BADD7
CADEEF
E8F1F8
0094D4
00A9DD
6FCCEA
C7EBF8
E9F6FB
00AB8E
00BBA5
67D7C9
C6EFE9
E9F9F6
EB3D1F
EC4F4E
F09395
F8D3D4
FCEDEE

Requirements
Should not have
• Colors not too light, darker colours preferred

```html
<!DOCTYPE html>
<html lang="en">
<head>
<meta charset="utf-8">
<title>Brenvik Business Card</title>
<link rel="stylesheet" href="https://fonts.googleapis.com/css2?family=Montserrat:wght@400;500;600;800&display=swap">
<style>
  :root {
    --backdrop: #cfd4d4;
    --paper: #f1f0ee;
    --ink: #1b1b1b;
    --ink-soft: #2e2e2e;
    --accent: #e0202a;
    --edge: #d0141c;
  }
  * { margin: 0; padding: 0; box-sizing: border-box; }
  html, body { width: 1200px; height: 881px; overflow: hidden; }
  body {
    background: var(--backdrop);
    font-family: "Montserrat", Arial, sans-serif;
    color: var(--ink);
    position: relative;
  }
  .card {
    position: absolute;
    top: 285px;
    width: 540px;
    height: 310px;
    background: var(--paper);
    border-bottom: 5px solid var(--edge);
    box-shadow: 0 14px 30px rgba(0,0,0,0.18);
  }
  .card--contact { left: 30px; }
  .card--brand { left: 630px; }

  /* contact side */
  .identity {
    position: absolute;
    right: 300px;
    top: 96px;
    text-align: right;
  }
  .identity__name {
    color: var(--accent);
    font-weight: 600;
    font-size: 27px;
    letter-spacing: 0.2px;
    white-space: nowrap;
  }
  .identity__role {
    margin-top: 6px;
    font-size: 14px;
    font-weight: 400;
    color: var(--ink-soft);
  }
  .divider {
    position: absolute;
    left: 256px;
    top: 96px;
    width: 2px;
    height: 66px;
    background: var(--accent);
  }
  .contact-list {
    position: absolute;
    left: 274px;
    top: 96px;
    list-style: none;
  }
  .contact-list li {
    display: flex;
    align-items: center;
    gap: 8px;
    font-size: 14px;
    line-height: 22px;
    color: var(--ink-soft);
    white-space: nowrap;
  }
  .contact-list svg { width: 12px; height: 12px; fill: var(--accent); flex: none; }
  .address {
    position: absolute;
    left: 110px;
    top: 232px;
    font-size: 14px;
    color: var(--ink-soft);
  }

  /* brand side */
  .brand {
    position: absolute;
    inset: 0;
    display: flex;
    align-items: center;
    justify-content: center;
    gap: 14px;
  }
  .brand__name {
    font-weight: 800;
    font-size: 84px;
    color: var(--ink);
    letter-spacing: -1px;
  }
  .brand__dot {
    width: 22px;
    height: 22px;
    border-radius: 50%;
    background: var(--accent);
    margin-top: 34px;
  }
</style>
</head>
<body>
  <section class="card card--contact">
    <div class="identity">
      <p class="identity__name">Daniel Hartwell</p>
      <p class="identity__role">Managing Director</p>
    </div>
    <div class="divider"></div>
    <ul class="contact-list">
      <li>
        <svg viewBox="0 0 24 24" aria-hidden="true"><path d="M6.6 10.8a15.1 15.1 0 0 0 6.6 6.6l2.2-2.2a1 1 0 0 1 1-.25 11.4 11.4 0 0 0 3.6.57 1 1 0 0 1 1 1V20a1 1 0 0 1-1 1A17 17 0 0 1 3 4a1 1 0 0 1 1-1h3.5a1 1 0 0 1 1 1c0 1.25.2 2.45.57 3.57a1 1 0 0 1-.25 1z"/></svg>
        555 018 246
      </li>
      <li>
        <svg viewBox="0 0 24 24" aria-hidden="true"><path d="M2 5h20v14H2zm2 2v.4l8 5.2 8-5.2V7z"/></svg>
        info@brenvikmail.com
      </li>
      <li>
        <svg viewBox="0 0 24 24" aria-hidden="true"><path d="M12 2a10 10 0 1 0 0 20 10 10 0 0 0 0-20zm6.9 9h-3a15 15 0 0 0-1.3-5.5A8 8 0 0 1 18.9 11zM12 4.1c.9 1.3 1.7 3.8 1.9 6.9h-3.8c.2-3.1 1-5.6 1.9-6.9zM9.4 5.5A15 15 0 0 0 8.1 11h-3a8 8 0 0 1 4.3-5.5zM5.1 13h3a15 15 0 0 0 1.3 5.5A8 8 0 0 1 5.1 13zM12 19.9c-.9-1.3-1.7-3.8-1.9-6.9h3.8c-.2 3.1-1 5.6-1.9 6.9zm2.6-1.4a15 15 0 0 0 1.3-5.5h3a8 8 0 0 1-4.3 5.5z"/></svg>
        www.brenvikwebsite.com
      </li>
    </ul>
    <p class="address">Your address, City State, Zip 1234</p>
  </section>

  <section class="card card--brand">
    <div class="brand">
      <span class="brand__name">Brenvik</span>
      <span class="brand__dot"></span>
    </div>
  </section>
</body>
</html>
```